Corvel Ridge New Website Design

We just changed our logo (thank you PlanHarbor) and company name change from Corvel Ridge Machining to Corvel Ridge Manufacturing. We do CNC Swiss screw machining and multi-axis machines. We make parts for many industries. We make large quantity production parts as well small R&D quantities. You can look at our current (outdated) website: http://www.corvelridgemachining.example to see what we do. We would like a WordPress site, including contact form for "request for quote" . We would also like it to be mobile friendly, and the ability to maintain it ourselves after it is finished I have included our new logo and fonts for references. We would like our site to convey the feeling of precision, capability, and trust worthiness with a very modern look. The new website address is www.corvelridge-mfg.example

Coding

Coded - Design and coding required

Number of Pages Required

5+ page

Font styles to use
Serif
Sans Serif
Other font styles liked:
• fronts included, not sure if they work

Colors

Designer to choose colors to be used in the design.

Requirements
Must have
• Contact Info, request for quote field

```html
<!DOCTYPE html>
<html lang="en">
<head>
<meta charset="utf-8">
<title>Corvel Ridge Manufacturing</title>
<link href="https://fonts.googleapis.com/css2?family=Lato:wght@300;400;700&display=swap" rel="stylesheet">
<style>
:root{
  --blue:#1f3f8c;
  --blue-dark:#183270;
  --ink:#444a52;
  --muted:#6b7078;
  --field:#e6e7e9;
  --line:#d6d8dc;
  --footer:#2f353c;
  --hero-a:#3a4656;
  --hero-b:#1c2430;
  --white:#ffffff;
}
*{box-sizing:border-box;margin:0;padding:0}
html,body{width:790px;height:1200px;overflow:hidden;background:var(--white)}
body{position:relative;font-family:'Lato',sans-serif;color:var(--ink)}
.abs{position:absolute}

/* header */
.site-header{left:164px;top:0;width:462px;height:31px;background:#f4f4f4;display:flex;align-items:center;justify-content:space-between;padding-left:10px;z-index:5}
.brand{display:flex;align-items:center;gap:5px;font-size:12px;font-weight:700;color:var(--blue)}
.brand-dot{width:9px;height:9px;border-radius:50%;background:var(--blue)}
.main-nav{display:flex;align-items:stretch;height:31px;font-size:6.4px}
.main-nav a{color:#444;text-decoration:none;padding:0 5px;display:flex;align-items:center}
.main-nav a.active{background:var(--blue);color:#fff;padding:0 6px;margin-right:3px}
.search-btn{width:14px;height:14px;border-radius:50%;background:var(--blue);align-self:center;margin:0 8px 0 3px;display:flex;align-items:center;justify-content:center}

/* hero */
.hero{left:0;top:0;width:790px;height:284px;background:radial-gradient(ellipse at 35% 30%,#5b6677 0%,var(--hero-a) 40%,var(--hero-b) 100%)}
.hero-title{left:163px;top:131px;font-size:22.5px;font-weight:400;color:#fff;line-height:27px}
.hero-title mark{background:var(--blue);color:#fff;padding:0 1px}
.quote-form{left:495px;top:75px;width:131px;height:165px;background:#f2f2f2;box-shadow:0 2px 6px rgba(0,0,0,.3)}
.quote-head{position:relative;height:42px;text-align:center;color:#fff;font-size:12.5px;font-weight:700;line-height:14px;padding-top:5px}
.quote-head svg{position:absolute;left:0;top:0;z-index:0}
.quote-head span{position:relative;z-index:1}
.field{margin:4px 5px 0;height:15px;background:var(--field);font-size:5px;color:#888;padding:5px 5px 0}
.field.msg{height:27px}
.send{margin:6px 5px 0;height:21px;background:var(--blue);color:#fff;font-size:8.5px;text-align:center;line-height:21px}

/* intro */
.intro-title{left:164px;top:319px;font-size:11.5px;font-weight:700;color:var(--blue)}
.intro-text{left:164px;top:340px;width:194px;font-size:5.6px;line-height:9.6px;color:#444}
.intro-callout{left:164px;top:408px;width:174px;height:28px;background:var(--blue);color:#fff;font-size:5.6px;line-height:7px;padding:7px 6px;border-radius:0 14px 14px 0;box-shadow:2px 2px 3px rgba(0,0,0,.25)}
.photo-shop{left:446px;top:302px;width:179px;height:119px;background:linear-gradient(160deg,#c9cccf,#8f9499 60%,#6d7176)}
.photo-desk{left:393px;top:365px;width:141px;height:93px;background:linear-gradient(150deg,#d8cdb4,#a59a84 55%,#4f5258);border:2px solid #fff}

/* industries */
.industries{left:0;top:476px;width:790px;height:136px;background:radial-gradient(ellipse at 50% 40%,#3c4656,#232a35 70%,#1a1f28)}
.industries-title{left:0;top:496px;width:790px;text-align:center;color:#fff;font-size:11.5px;font-weight:700}
.industry{top:538px;width:70px;text-align:center;color:#fff;font-size:6.6px}
.industry .ico{width:27px;height:27px;border-radius:50%;background:#fff;margin:0 auto 5px;display:flex;align-items:center;justify-content:center}

/* work */
.work-title{left:0;top:624px;width:790px;text-align:center;color:var(--blue);font-size:11.5px;font-weight:700}
.work-text{left:255px;top:643px;width:280px;text-align:center;font-size:5.6px;line-height:8.6px;color:#666}
.work-card{top:677px;width:111px;height:92px;border:1px solid var(--line);background:#fff;display:flex;align-items:center;justify-content:center}
.work-card .part{width:72px;height:60px;border-radius:8px}
.pager{top:777px;width:10px;height:10px;border:1px solid #999;display:flex;align-items:center;justify-content:center}

/* about */
.about-band{left:0;top:802px;width:790px;height:170px;background:linear-gradient(100deg,#cfd2d5,#a6abb1 45%,#c8cbcf 70%,#e2e3e5)}
.about-card{left:202px;top:903px;width:386px;height:161px;background:#fff;text-align:center;box-shadow:0 6px 6px -5px rgba(0,0,0,.2)}
.about-card h2{font-size:13.5px;font-weight:700;color:var(--blue);margin-top:11px}
.about-card .rule{width:16px;height:1px;background:#333;margin:4px auto 8px}
.about-card p{font-size:5.2px;line-height:8px;color:#666;padding:0 26px;margin-bottom:8px}
.btn{display:inline-block;width:61px;height:16px;line-height:16px;background:var(--blue);color:#fff;font-size:6px;font-weight:700}

/* testimonials */
.testimonial{left:259px;top:1078px;width:272px;height:88px;background:var(--blue);text-align:center;color:#fff}
.testimonial h2{font-size:13px;font-weight:700;margin-top:11px}
.testimonial .quote{font-size:6.6px;line-height:10px;margin-top:3px;padding:0 40px}
.testimonial .who{font-size:6.2px;line-height:8px;margin-top:6px}
.qmark{width:19px;height:19px;border-radius:50%;background:#fff;color:var(--blue);font-size:14px;font-weight:700;text-align:center;line-height:22px}

/* footer */
.site-footer{left:0;top:1186px;width:790px;height:14px;background:var(--footer);color:#fff;font-size:4.8px;line-height:14px}
.site-footer .copy{position:absolute;left:164px}
.site-footer .links{position:absolute;right:164px}
</style>
</head>
<body>

<section class="abs hero" role="img" aria-label="Close-up photo of a CNC machine cutting metal parts with chips"></section>

<header class="abs site-header">
  <div class="brand"><span class="brand-dot"></span>Corvel Ridge</div>
  <nav class="main-nav">
    <a class="active">Home</a><a>Services</a><a>Equipment</a><a>Quality</a><a>Our work</a><a>About us</a><a>Contact us</a>
    <span class="search-btn"><svg width="7" height="7" viewBox="0 0 10 10"><circle cx="4" cy="4" r="3" fill="none" stroke="#fff" stroke-width="1.5"/><line x1="6.2" y1="6.2" x2="9" y2="9" stroke="#fff" stroke-width="1.5"/></svg></span>
  </nav>
</header>

<h1 class="abs hero-title">From <mark>Blueprint</mark> to Reality<br>Better than you <mark>Expected</mark></h1>

<form class="abs quote-form">
  <div class="quote-head">
    <svg width="131" height="42" viewBox="0 0 131 42"><path d="M0 0H131V34Q65 48 0 34Z" fill="var(--blue)"/></svg>
    <span>Request a<br>Quote</span>
  </div>
  <div class="field">Name</div>
  <div class="field">Email</div>
  <div class="field">Company name</div>
  <div class="field msg">Message</div>
  <div class="send">SEND</div>
</form>

<h2 class="abs intro-title">When less is More</h2>
<p class="abs intro-text">Corvel Ridge Machining Company is a high quality machining resource providing friendly service, fast turnaround times, and engineering expertise, at competitive pricing. With almost 20 years of experience in the industry, Corvel Ridge utilizes certified state of the art equipment partnered with top professionals to maximize the value and quality in your product.</p>
<div class="abs intro-callout">Specializing in precision, Corvel Ridge will provide you with superior products, at affordable prices.</div>
<div class="abs photo-shop" role="img" aria-label="Photo of the machine shop floor with rows of CNC machines"></div>
<div class="abs photo-desk" role="img" aria-label="Photo of a technician at a measuring station computer"></div>

<section class="abs industries" role="img" aria-label="Dark photo of interlocking gears"></section>
<h2 class="abs industries-title">Industries Served</h2>
<div class="abs industry" style="left:146px"><div class="ico"><svg width="15" height="15" viewBox="0 0 20 20" fill="none" stroke="var(--blue)" stroke-width="1.2"><path d="M3 13l5-1 4-6 3-3 1 1-3 3-1 6-2 1v-4l-3 2v3l-1 1-1-3z"/></svg></div>Aerospace</div>
<div class="abs industry" style="left:217px"><div class="ico"><svg width="15" height="15" viewBox="0 0 20 20" fill="none" stroke="var(--blue)" stroke-width="1.2"><rect x="6" y="6" width="8" height="8"/><path d="M8 3v3M12 3v3M8 14v3M12 14v3M3 8h3M3 12h3M14 8h3M14 12h3"/></svg></div>Electronics</div>
<div class="abs industry" style="left:290px"><div class="ico"><svg width="15" height="15" viewBox="0 0 20 20" fill="none" stroke="var(--blue)" stroke-width="1.2"><circle cx="10" cy="10" r="5"/><circle cx="10" cy="10" r="2"/><path d="M10 2v3M10 15v3M2 10h3M15 10h3M4 4l2 2M14 14l2 2M16 4l-2 2M4 16l2-2"/></svg></div>Automotive</div>
<div class="abs industry" style="left:361px"><div class="ico"><svg width="15" height="15" viewBox="0 0 20 20" fill="none" stroke="var(--blue)" stroke-width="1.2"><circle cx="10" cy="4" r="1.6"/><path d="M10 6v11M6 9h8M4 12q1 5 6 5t6-5"/></svg></div>Marine</div>
<div class="abs industry" style="left:433px"><div class="ico"><svg width="15" height="15" viewBox="0 0 20 20" fill="none" stroke="var(--blue)" stroke-width="1.2"><rect x="3" y="4" width="14" height="9"/><path d="M8 13v3M12 13v3M6 16h8"/></svg></div>Computer</div>
<div class="abs industry" style="left:505px"><div class="ico"><svg width="15" height="15" viewBox="0 0 20 20" fill="none" stroke="var(--blue)" stroke-width="1.2"><path d="M5 3v5a3 3 0 006 0V3M8 11v3a3 3 0 006 0v-2"/><circle cx="14" cy="10" r="1.6"/></svg></div>Medical</div>
<div class="abs industry" style="left:577px"><div class="ico"><svg width="15" height="15" viewBox="0 0 20 20" fill="none" stroke="var(--blue)" stroke-width="1.2"><path d="M6 3c-3 0-4 3-3 6 1 2 1 4 2 7 1 2 2 0 3-3 1-2 3-2 4 0 1 3 2 5 3 3 1-3 1-5 2-7 1-3 0-6-3-6-2 0-3 1-4 1S8 3 6 3z"/></svg></div>Dental</div>

<h2 class="abs work-title">Our Work</h2>
<p class="abs work-text">Corvel Ridge has provided some of the most innovative results for clients, among many different industries. Below are just some of the quality products we were able to produce:</p>
<div class="abs work-card" style="left:164px"><div class="part" role="img" aria-label="Photo of a machined black and steel cylindrical fitting" style="background:linear-gradient(135deg,#a8a8a8,#2a2a2a)"></div></div>
<div class="abs work-card" style="left:281px"><div class="part" role="img" aria-label="Photo of a bronze-toned machined dome housing" style="background:linear-gradient(135deg,#b6a47a,#6b5c3c)"></div></div>
<div class="abs work-card" style="left:398px"><div class="part" role="img" aria-label="Photo of an aluminium flanged connector body" style="background:linear-gradient(135deg,#dcdcdc,#7c7f83)"></div></div>
<div class="abs work-card" style="left:514px"><div class="part" role="img" aria-label="Photo of a polished steel threaded cylinder" style="background:linear-gradient(135deg,#e6e6e6,#8a8d90)"></div></div>
<div class="abs pager" style="left:385px"><svg width="5" height="6" viewBox="0 0 5 6"><path d="M4 0L1 3l3 3" fill="none" stroke="#999"/></svg></div>
<div class="abs pager" style="left:396px;border-color:var(--blue)"><svg width="5" height="6" viewBox="0 0 5 6"><path d="M1 0l3 3-3 3" fill="none" stroke="var(--blue)"/></svg></div>

<section class="abs about-band" role="img" aria-label="Photo of Swiss-type CNC lathes in the production shop"></section>
<section class="abs about-card">
  <h2>About Us</h2>
  <div class="rule"></div>
  <p>Founded in 1996, Corvel Ridge Machining Inc. was established at the hands of engineering experts, trying to develop a high quality solution for the machining industry. Corvel Ridge Machining Inc. utilizes state of the art, fully automated, equipment. This enables us to provide quick turnaround times, without compromising the quality of the product.</p>
  <p>We prides ourselves on our friendly and efficient customer service, making sure we meet the needs and standards of our valuable customers. With a knowledgeable team, we provide companies with invaluable support during the engineering process, producing favorable results and always leave customers extremely gratified.</p>
  <p>Here at Corvel Ridge, we strive to provide our clients with loyalty in a partner, where a handshake is more than a greeting; it is the hopeful development of a strong relationship.</p>
  <span class="btn">Read More</span>
</section>

<section class="abs testimonial">
  <h2>Testimonials</h2>
  <p class="quote">I love working with engineers. Finding ways to make their parts less expensive is a puzzle I never get tired of solving.</p>
  <p class="who">Dalen Whitcombe<br>Founder</p>
</section>
<div class="abs qmark" style="left:496px;top:1069px">&#8221;</div>
<div class="abs qmark" style="left:273px;top:1155px">&#8221;</div>

<footer class="abs site-footer">
  <span class="copy">© All rights reserved</span>
  <span class="links">Sitemap &nbsp;|&nbsp; Contact us</span>
</footer>

</body>
</html>
```